Brochure Design Project

We need a brochure design for an existing small Architectural Design company. The brochure needs to be in 2 pages in A4 format to be emailed to clients as a PDF. We have written the copy for the brochure, but we are very open to any suggestions you may have here. Our logo has been designed and is attached. This design will also need to be developed into a double sided "tri-fold" A4 brochure which will printed and distributed to perspective clients. We would like portrait pictures for the key staff next to each description, but do not have these as yet. Use any photos contained on our website www.plantrace.net.nz which you think will enhance the brochure. The brochure should reflect out website design and style.
Updates

Have changed the text file. Make sure the text file is called "profile kellow partners July 11".

Industry/Entity Type

It Company

Requirements
Must have
• Please use all the copy and logos provided. Design of brochure should fit with our existing logo. Must have a modern look with a high emphasis on design.
Nice to have
• As many photos as possible, without cluttering.
Should not have
• Must have a modern look with a high emphasis on design.

```html
<!DOCTYPE html>
<html lang="en">
<head>
<meta charset="utf-8">
<title>Kellow Partners – Services</title>
<link href="https://fonts.googleapis.com/css2?family=Open+Sans:ital,wght@0,400;0,600;1,700&display=swap" rel="stylesheet">
<style>
  :root {
    --bg: #000000;
    --panel: #1f2727;
    --lime: #8cc63f;
    --line-dark: #34443a;
    --text: #ffffff;
    --muted: #c9cfcf;
    --dusk-top: #3d6da6;
    --dusk-bottom: #6b5a3e;
    --day-top: #eef0f0;
    --day-bottom: #8e9496;
  }
  * { margin: 0; padding: 0; box-sizing: border-box; }
  html, body { width: 849px; height: 1200px; overflow: hidden; background: var(--bg); }
  .page {
    position: relative; width: 849px; height: 1200px; background: var(--bg);
    font-family: "Open Sans", Arial, sans-serif; color: var(--text);
  }
  .grid-lines { position: absolute; inset: 0; }
  .brand { position: absolute; left: 90px; top: 36px; }
  .brand-name { font-weight: 600; font-size: 31px; letter-spacing: 1px; line-height: 1; color: var(--text); }
  .brand-line { margin-top: 8px; font-size: 7px; letter-spacing: 0.5px; color: var(--muted); font-weight: 400; }
  .badge { position: absolute; left: 771px; top: 4px; width: 74px; height: 74px; border-radius: 50%; background: var(--lime); border: 3px solid #ffffff; }
  .panel { position: absolute; background: var(--panel); font-style: italic; font-weight: 700; }
  .services { left: 101px; top: 106px; width: 587px; height: 304px; padding: 12px 18px; }
  .panel-title { font-size: 19px; line-height: 1.2; margin-bottom: 6px; }
  .services-intro { font-size: 14.5px; line-height: 20px; }
  .services-list { list-style: none; margin-left: 36px; font-size: 14.5px; }
  .services-list li { line-height: 20.6px; display: flex; align-items: center; }
  .services-list li::before {
    content: ""; width: 10px; height: 10px; margin-right: 6px; flex: none;
    background: linear-gradient(135deg, #ffffff, #8a8f8f); border: 1px solid #5c6262;
  }
  .photo { position: absolute; }
  .photo-dusk { left: 474px; top: 410px; width: 366px; height: 243px; background: linear-gradient(180deg, var(--dusk-top) 0%, #8aa3c0 35%, #c9b89a 60%, var(--dusk-bottom) 100%); }
  .photo-day { left: 87px; top: 660px; width: 436px; height: 278px; background: linear-gradient(180deg, var(--day-top) 0%, #c9cccd 55%, var(--day-bottom) 100%); }
  .contact { left: 228px; top: 960px; width: 386px; height: 215px; padding: 12px 10px; }
  .contact-list { margin-left: 27px; font-size: 14.5px; line-height: 21px; }
  .contact-row { display: flex; }
  .contact-row dt { width: 128px; }
</style>
</head>
<body>
<div class="page">
  <svg class="grid-lines" width="849" height="1200" viewBox="0 0 849 1200" aria-hidden="true">
    <g fill="none" stroke="var(--line-dark)" stroke-width="3">
      <path d="M0 30 H770"/>
      <path d="M738 30 V878 L849 930"/>
      <path d="M0 878 H738"/>
    </g>
    <g fill="none" stroke="var(--lime)" stroke-width="3">
      <path d="M77 0 V1200"/>
      <path d="M0 76 H770"/>
      <path d="M0 195 H101"/>
      <path d="M0 1020 H228"/>
      <path d="M336 410 V660"/>
      <path d="M688 218 H763 V780 H523"/>
      <rect x="69" y="68" width="16" height="16"/>
      <rect x="69" y="187" width="16" height="16"/>
      <rect x="69" y="1012" width="16" height="16"/>
    </g>
  </svg>

  <div class="brand">
    <div class="brand-name">kellow partners</div>
    <div class="brand-line">P 07 821 4406 · www.plantrace.net</div>
  </div>
  <div class="badge" aria-hidden="true"></div>

  <section class="panel services">
    <h2 class="panel-title">SERVICES:</h2>
    <p class="services-intro">Kellow Partners has the skills and ability to provide the following services:</p>
    <ul class="services-list">
      <li>Site inspection, assessment and feasibility.</li>
      <li>Conceptual design.</li>
      <li>Secondary Consultant liaison and management.</li>
      <li>3D Modelling and Renders.</li>
      <li>Resource Consent Documentation.</li>
      <li>Developed design.</li>
      <li>Construction documentation.</li>
      <li>Tender Process Management.</li>
      <li>Site observation.</li>
      <li>Contract administration.</li>
      <li>Green technology Analysis.</li>
    </ul>
  </section>

  <div class="photo photo-dusk" role="img" aria-label="Modern rendered house lit at dusk with garage doors and evening sky"></div>
  <div class="photo photo-day" role="img" aria-label="Contemporary two-storey grey house with angled panels and louvres in daylight"></div>

  <section class="panel contact">
    <h2 class="panel-title">Contact :</h2>
    <dl class="contact-list">
      <div class="contact-row"><dt>PO Box 48620</dt></div>
      <div class="contact-row"><dt>Hamilton 3216</dt></div>
      <div class="contact-row"><dt>New Zealand</dt></div>
      <div class="contact-row"><dt>Ph</dt><dd>64 7 8214406</dd></div>
      <div class="contact-row"><dt>Fax</dt><dd>64 7 8214418</dd></div>
      <div class="contact-row"><dt>Mob</dt><dd>021556730</dd></div>
      <div class="contact-row"><dt>email:</dt><dd>admin@plantrace.net.nz</dd></div>
      <div class="contact-row"><dt>Website:</dt><dd>www.plantrace.net.nz</dd></div>
    </dl>
  </section>
</div>
</body>
</html>
```